依頼詳細
サイト構成・基本的な要件については
https://zuvexo.example/boards/R7pQ2mXa9TkWvHcY/B58F3
をご参照ください。

ただ、レイアウトについては、各コンテンツへの導線が確保されていれば、
上記レイアウト案を必ず守る必要はございません。
また、当方jqueryを使用したコーディングも可能です。

提出の写真素材は
https://qlbox.example/T9wRkA
上記のものをご利用いただければ幸いです。

現在、素材があまり集まっていないため、
http://fotmira.example/
などから、10000円程度までならこちらにて購入可能です。
カンプデータにて作成頂き、納品時に当方にて購入したデータに差し替えていただければと存じます。

https://images.velonta.example/jp/
についても定期購入しておりますので、
5点ほどでしたら取得可能です。

また、既存サイト
https://www.harimoku.example/
に使用されている画像は自由にご利用ください。

【参考サイト】
https://www.tzr-worldwide.example/jp/
https://morifusa.example/
https://hotarubako.example/
https://www.calmfield.example/
https://www.yosetabi.example/

写真を大きく見せ、
高級感があり、訴求力の高いデザインを希望します。

色合いは、現在のサイト同様、
モノトーンをベースに、差し色を使用する場合は1色程度、
シックで高級感のある色合いを希望いたします。
サイトURL
ページ数
1ページ
希望イメージ
シンプル 複雑
単色 カラフル
暗い 明るい
日常 高級
遊び心 厳粛
未来的 伝統的
女性的 男性的
希望する色
グレー系
納品ファイル
• 高解像度JPG (.jpg)
• フォトショップ形式 (.psd)
補足説明
提出の写真素材は
https://qlbox.example/T9wRkA
上記アップロードしたものをご利用いただければ幸いです。

現在、素材があまり集まっていないため、
http://fotmira.example/
についても定期購入しておりますので、
5点ほどでしたら取得可能です。

納品データはPSDのほか
XDの提出でも問題ございません。

制作に関してご不明な点がございましたら
お気軽にお申し付けください。

何卒宜しくお願い致します。

```html
<!DOCTYPE html>
<html lang="ja">
<head>
<meta charset="utf-8">
<title>HARIMOKU | 快適居住空間の演出</title>
<link rel="stylesheet" href="https://fonts.googleapis.com/css2?family=Noto+Serif+JP:wght@400;500&family=Cormorant+Garamond:wght@300;400&display=swap">
<style>
:root{
  --bg:#e5e3df;
  --paper:#f3f2ef;
  --ink:#3f3d3a;
  --muted:#7d7a75;
  --line:#b9b5ae;
  --gold:#bca67a;
  --dark:#5d5c5a;
  --photo-a:#3a332d;
  --photo-b:#8b7a68;
}
*{margin:0;padding:0;box-sizing:border-box}
html,body{width:1200px;height:3576px;overflow:hidden}
body{background:var(--bg);color:var(--ink);font-family:"Noto Serif JP",serif;font-size:13px;line-height:2;position:relative}
.abs{position:absolute}
.photo{background:linear-gradient(135deg,var(--photo-a),var(--photo-b))}
.photo.light{background:linear-gradient(135deg,#d8d3cb,#9b8f80)}
.photo.warm{background:linear-gradient(135deg,#4a3526,#a07a55)}
/* header */
.brand{left:100px;top:0;width:90px;height:80px;background:var(--gold);color:#fff;display:flex;flex-direction:column;align-items:center;justify-content:center;font-size:11px;letter-spacing:.06em;line-height:1.3;text-align:center}
.brand small{font-size:7px;letter-spacing:.08em}
.header-tel{left:660px;top:20px;font-family:"Cormorant Garamond",serif;font-size:24px;line-height:1;display:flex;align-items:center;gap:6px}
.header-hours{left:660px;top:48px;font-size:10px;color:var(--muted)}
.btn{border:1px solid var(--ink);display:flex;align-items:center;justify-content:center;font-size:11px;letter-spacing:.08em;color:var(--ink);background:transparent}
.header-btn{left:930px;top:30px;width:240px;height:44px}
/* hero */
.hero-photo{left:100px;top:80px;width:500px;height:580px}
.hero-copy{left:630px;top:340px;font-family:"Cormorant Garamond",serif;font-weight:300;font-size:40px;line-height:1.15;color:#c4c0b9}
.hero-title{left:632px;top:500px;font-size:20px;letter-spacing:.12em}
.hero-lead{left:632px;top:540px;width:480px;font-size:12px;color:var(--muted)}
/* intro */
.intro-head{left:100px;top:700px;font-size:19px;line-height:1.8;letter-spacing:.05em}
.intro-text{left:100px;top:790px;width:880px;font-size:12px;color:var(--muted);line-height:2.1}
.intro-text p{margin-bottom:18px}
/* services */
.services-band{left:0;top:1200px;width:980px;height:80px;background:var(--paper)}
.services-band2{left:0;top:1280px;width:1200px;height:700px;background:var(--paper)}
.services-head{left:100px;top:1250px;font-size:18px;line-height:1.8;letter-spacing:.05em}
.grid{left:100px;width:1000px;display:grid;grid-template-columns:repeat(4,220px);column-gap:40px}
.grid .thumb{height:220px}
.grid .label{margin-top:16px;font-size:12px;padding-bottom:6px;border-bottom:1px solid var(--line);width:fit-content;padding-right:20px}
.more{font-size:12px;display:flex;align-items:center;gap:10px}
/* works */
.works-band{left:240px;top:2040px;width:960px;height:420px;background:#d7d4cf}
.works-head{right:100px;top:2100px;font-size:18px;letter-spacing:.1em}
.works-row{left:100px;top:2180px;display:flex;gap:40px}
.works-row div{width:220px;height:280px;flex:none}
/* cta */
.cta{left:0;top:2560px;width:1200px;height:230px;background:linear-gradient(90deg,#5c5955,#77736d 60%,#8e8a84)}
.cta-lead{left:0;right:0;top:2595px;text-align:center;font-size:17px;color:#fff;letter-spacing:.08em}
.cta-tel{left:0;right:0;top:2650px;text-align:center;font-family:"Cormorant Garamond",serif;font-size:36px;color:#fff;line-height:1}
.cta-btn{left:450px;top:2720px;width:300px;height:46px;background:#fff;border:none}
/* news */
.news-head{left:100px;top:2930px;font-size:15px;letter-spacing:.1em}
.news-all{left:100px;top:2975px;font-size:11px;padding-bottom:4px;border-bottom:1px solid var(--line);width:90px}
.news-list{left:270px;top:2945px;width:830px;list-style:none}
.news-list li{display:flex;gap:30px;font-size:12px;padding:16px 0;border-bottom:1px solid var(--line);color:var(--muted)}
.news-list li:first-child{border-top:1px solid var(--line)}
/* footer */
.footer{left:0;top:3216px;width:1200px;height:360px;background:var(--dark)}
.footer-nav{left:100px;top:3238px;display:flex;gap:22px;font-size:11px;color:#e8e6e2}
.footer-brand{left:270px;top:3328px;width:140px;color:#fff;font-size:17px;letter-spacing:.12em;line-height:1.2;text-align:center}
.footer-brand small{display:block;font-size:8px;letter-spacing:.1em}
.footer-addr{left:440px;top:3322px;width:300px;font-size:10.5px;line-height:1.9;color:#e8e6e2}
.footer-btn{left:800px;width:260px;height:40px;border-color:#e8e6e2;color:#e8e6e2;font-size:10.5px}
.copyright{left:0;right:0;top:3520px;text-align:center;font-size:10px;color:#cfcdc9}
</style>
</head>
<body>
<header>
  <div class="abs brand">HARIMOKU<small>space design</small></div>
  <div class="abs header-tel"><svg width="18" height="18" viewBox="0 0 24 24"><path d="M6.6 10.8a15 15 0 006.6 6.6l2.2-2.2c.3-.3.7-.4 1-.2 1.1.4 2.3.6 3.6.6.6 0 1 .4 1 1V20c0 .6-.4 1-1 1A17 17 0 013 4c0-.6.4-1 1-1h3.5c.6 0 1 .4 1 1 0 1.3.2 2.5.6 3.6.1.3 0 .7-.2 1z" fill="#3f3d3a"/></svg>0120-418-627</div>
  <div class="abs header-hours">受付時間 9:00〜18:00（土日祝除く）</div>
  <a class="abs btn header-btn">資料請求・お問い合わせはこちら</a>
</header>

<section>
  <div class="abs hero-photo photo light" role="img" aria-label="モダンなリビングルームの内観写真"></div>
  <p class="abs hero-copy">Production of Comfortable<br>Living Space</p>
  <h1 class="abs hero-title">快適居住空間の演出</h1>
  <p class="abs hero-lead">ひとりひとりに合った住まいを、オーダーメイドで作り上げていきます。<br>素材やデザインにこだわり、上質で居心地の良い住空間を、<br>職人の確かな技術でお届けいたします。</p>
</section>

<section>
  <h2 class="abs intro-head">ハリモクは少数精鋭主義にこだわり、<br>一人ひとりにあった住空間をご提案しています</h2>
  <div class="abs intro-text">
    <p>1998年、株式会社ハリモクとして創業して以来、住宅・店舗・オフィスなどのリフォームやデザインを手掛けてまいりました。企画・設計・施工・アフターメンテナンスまでを一貫して自社で行うことで、お客様のご要望を細部まで形にしています。<br>また、経験を積んだ担当者がお打ち合わせから完成まで責任を持って対応し、デザイン性と機能性を兼ね備えた住まいをお届けします。</p>
    <p>素材選びから照明計画に至るまで、住まう方の暮らしを第一に考えたご提案を心掛けております。少人数だからこそできる丁寧な対応で、<br>一件一件のお住まいと真摯に向き合い、長く愛される空間づくりを目指しております。</p>
    <p>リフォームに関するご相談は、どんな小さなことでもお気軽にお問い合わせください。<br>スタッフ一同、心よりお待ちしております。</p>
  </div>
</section>

<section>
  <div class="abs services-band"></div>
  <div class="abs services-band2"></div>
  <h2 class="abs services-head">以下のご要望に対応いたします。<br>お気軽にご相談ください</h2>
  <div class="abs grid" style="top:1352px">
    <div><div class="thumb photo" role="img" aria-label="石目調の壁面とリビングの写真"></div><p class="label">デザインリフォーム</p></div>
    <div><div class="thumb photo warm" role="img" aria-label="マンションの室内写真"></div><p class="label">マンションリフォーム</p></div>
    <div><div class="thumb photo light" role="img" aria-label="洗面台と浴室の写真"></div><p class="label">浴室・洗面・トイレリフォーム</p></div>
    <div><div class="thumb photo light" role="img" aria-label="キッチンの写真"></div><p class="label">キッチンリフォーム</p></div>
  </div>
  <div class="abs grid" style="top:1640px">
    <div><div class="thumb photo light" role="img" aria-label="玄関と収納の写真"></div><p class="label">玄関・エントランス</p></div>
    <div><div class="thumb photo warm" role="img" aria-label="木の階段と吹き抜けの写真"></div><p class="label">リノベーション</p></div>
    <div><div class="thumb photo warm" role="img" aria-label="照明の映える室内の写真"></div><p class="label">照明・インテリア</p></div>
    <div><div class="thumb photo light" role="img" aria-label="ソファのある居室の写真"></div><p class="label">店舗リフォーム</p></div>
  </div>
  <a class="abs more" style="left:960px;top:1928px">施工事例をみる<svg width="30" height="8"><path d="M0 6h28l-6-5" stroke="#3f3d3a" fill="none"/></svg></a>
</section>

<section>
  <div class="abs works-band"></div>
  <h2 class="abs works-head">最新施工例</h2>
  <div class="abs works-row">
    <div class="photo" role="img" aria-label="夜景の見える室内の施工写真"></div>
    <div class="photo warm" role="img" aria-label="木目の室内の施工写真"></div>
    <div class="photo light" role="img" aria-label="明るいリビングの施工写真"></div>
    <div class="photo" role="img" aria-label="高層階リビングの施工写真"></div>
    <div class="photo warm" role="img" aria-label="ダイニングの施工写真"></div>
  </div>
</section>

<section>
  <div class="abs cta" role="img" aria-label="ソファのある室内の写真を背景にした帯"></div>
  <p class="abs cta-lead">見積無料！まずはお気軽にお問い合わせください</p>
  <p class="abs cta-tel"><svg width="26" height="26" viewBox="0 0 24 24" style="vertical-align:-3px"><path d="M6.6 10.8a15 15 0 006.6 6.6l2.2-2.2c.3-.3.7-.4 1-.2 1.1.4 2.3.6 3.6.6.6 0 1 .4 1 1V20c0 .6-.4 1-1 1A17 17 0 013 4c0-.6.4-1 1-1h3.5c.6 0 1 .4 1 1 0 1.3.2 2.5.6 3.6.1.3 0 .7-.2 1z" fill="#fff"/></svg> 0120-418-627</p>
  <a class="abs btn cta-btn">お問い合わせはこちら</a>
</section>

<section>
  <h2 class="abs news-head">最新情報</h2>
  <a class="abs news-all">すべて見る →</a>
  <ul class="abs news-list">
    <li><span>2020.12.21</span><span>新着情報のお知らせ。年末年始の営業日についてご案内いたします。</span></li>
    <li><span>2020.12.11</span><span>新着情報のお知らせ。施工事例に新しい住まいを追加いたしました。</span></li>
    <li><span>2020.12.01</span><span>新着情報のお知らせ。ショールームの見学予約を受け付けております。</span></li>
  </ul>
</section>

<footer>
  <div class="abs footer"></div>
  <nav class="abs footer-nav"><span>トップページ</span><span>施工事例</span><span>よくある質問</span><span>施工の流れ</span><span>会社概要</span><span>お問い合わせ</span><span>サイトマップ</span><span>プライバシーポリシー</span><span>採用情報</span></nav>
  <div class="abs footer-brand">HARIMOKU<small>space design</small></div>
  <p class="abs footer-addr">〒100-0000 東京都港区青葉町1-2-3 青葉ビル4F<br>TEL：03-0000-4186<br>FAX：03-0000-4187</p>
  <a class="abs btn footer-btn" style="top:3324px">資料請求・お問い合わせはこちら</a>
  <a class="abs btn footer-btn" style="top:3380px">メールでのお問い合わせはこちら</a>
  <p class="abs copyright">Copyright © 2020 株式会社ハリモク All Rights Reserved.</p>
</footer>
</body>
</html>
```